CBD Company needs bag design made

Our company is creating CBD gummies which we need a design based off the dimensions of the AI file provided. I have included some base designs for basic ideas. The flavors are as follows "Blue Raspberry" .. "Tropical Fruit" .. "Fizzlot" (which is a sour strawberry) and "Watermelon" I included the mock ups of the bags as well as some zoomed in pictures of two the labels as well to give a little better of a reference. Our company name is Corvanta which we would like instead of Dapplets (Corvanta logo attached). The final design should display what's in each bag (4 separate bag designs) with images depicting that in addition the to Corvana Logo(ai attached). I attached the nutritional facts as well which should match the color schemes of each flavor (where the blue color is in the image attached to match the flavor example: Blue Raspberry = blue) this will be located on the back of the bag.

```html
<!DOCTYPE html>
<html lang="en">
<head>
<meta charset="utf-8">
<title>Corvanta CBD Gummies – Bag Fronts</title>
<link rel="stylesheet" href="https://fonts.googleapis.com/css2?family=Almendra:wght@700&family=Open+Sans:wght@400;600;700;800&display=swap">
<style>
  :root {
    --page-bg: #ffffff;
    --pink-deep: #d77cc6;
    --pink-soft: #f6dcef;
    --pink-title: #a8388f;
    --lilac-deep: #a59fd8;
    --lilac-soft: #ecebf7;
    --lilac-title: #4b4676;
    --brand-green: #8db470;
    --badge-green: #2f6a2a;
    --text-dark: #3a2a33;
    --band-white: rgba(255,255,255,0.85);
  }
  * { margin: 0; padding: 0; box-sizing: border-box; }
  html, body {
    width: 1200px; height: 970px; overflow: hidden;
    background: var(--page-bg);
    font-family: "Open Sans", sans-serif;
  }
  .canvas { position: relative; width: 1200px; height: 970px; }
  .bag {
    position: absolute; top: 120px; width: 464px; height: 720px;
    overflow: hidden;
  }
  .bag--fizzlot { left: 112px; }
  .bag--blue { left: 632px; }
  .bag-art { position: absolute; inset: 0; width: 100%; height: 100%; }

  .brand {
    position: absolute; left: 0; right: 0; top: 188px;
    text-align: center; color: var(--brand-green);
    font-weight: 400; font-size: 27px; line-height: 24px;
  }
  .brand-dot {
    display: block; width: 40px; height: 40px; margin: 0 auto 12px;
    border-radius: 50%; background: var(--brand-green);
  }
  .flavor-title {
    position: absolute; left: 0; right: 0; text-align: center;
    font-family: "Almendra", serif; font-weight: 700; line-height: 1;
  }
  .bag--fizzlot .flavor-title { top: 300px; font-size: 50px; color: var(--pink-title); }
  .bag--blue .flavor-title { top: 312px; font-size: 36px; color: var(--lilac-title); }
  .product-type {
    position: absolute; left: 0; right: 0; top: 358px; text-align: center;
    font-weight: 700; font-size: 24px; letter-spacing: 0.5px; color: var(--brand-green);
  }
  .bag--blue .product-type { top: 352px; }
  .extract-pill {
    position: absolute; left: 50%; top: 398px; transform: translateX(-50%);
    padding: 2px 8px; border-radius: 6px; color: #fff;
    font-size: 8.5px; font-weight: 700; white-space: nowrap;
  }
  .bag--fizzlot .extract-pill { background: var(--pink-title); }
  .bag--blue .extract-pill { background: var(--lilac-title); }
  .flavor-visual {
    position: absolute; left: 156px; top: 424px; width: 164px; height: 192px;
    border-radius: 40% 40% 30% 30%;
  }
  .bag--fizzlot .flavor-visual { background: radial-gradient(circle at 50% 40%, #e0443f, #a04d8e 60%, #c98fbf); }
  .bag--blue .flavor-visual { background: radial-gradient(circle at 50% 40%, #5a6fc8, #4b3f7c 60%, #9a94cc); }
  .net-weight {
    position: absolute; left: 76px; top: 580px;
    font-size: 13px; font-weight: 600; line-height: 18px; color: var(--text-dark);
  }
  .website {
    position: absolute; left: 76px; top: 626px;
    font-size: 10.5px; font-weight: 600; color: var(--text-dark);
  }
  .strength-badge {
    position: absolute; left: 326px; top: 600px; width: 92px; height: 92px;
    border-radius: 50%; background: rgba(255,255,255,0.9);
    display: flex; flex-direction: column; align-items: center; justify-content: center;
    color: var(--badge-green); font-weight: 800; line-height: 1;
  }
  .strength-badge .mg { font-size: 16px; margin-top: 12px; }
  .strength-badge .cbd { font-size: 26px; }
</style>
</head>
<body>
<main class="canvas">

  <section class="bag bag--fizzlot">
    <svg class="bag-art" viewBox="0 0 464 720" preserveAspectRatio="none" aria-hidden="true">
      <defs>
        <linearGradient id="pinkBody" x1="0" y1="0" x2="1" y2="1">
          <stop offset="0" stop-color="#f3c6e6"/>
          <stop offset="0.45" stop-color="#fbeaf5"/>
          <stop offset="1" stop-color="#dd87cb"/>
        </linearGradient>
      </defs>
      <rect width="464" height="720" fill="url(#pinkBody)"/>
      <rect x="0" y="0" width="464" height="110" fill="#f2bfe2" opacity="0.6"/>
      <rect x="16" y="66" width="432" height="4" fill="#ffffff" opacity="0.8"/>
      <polygon points="0,220 464,20 464,60 0,280" fill="#ffffff" opacity="0.55"/>
      <polygon points="0,300 464,70 464,90 0,330" fill="#e08cce" opacity="0.5"/>
      <polygon points="0,720 0,690 464,520 464,560 120,720" fill="#ffffff" opacity="0.85"/>
      <polygon points="200,720 464,600 464,640 290,720" fill="#ffffff" opacity="0.7"/>
    </svg>
    <div class="brand"><span class="brand-dot"></span>Corvanta<br>CBD</div>
    <h1 class="flavor-title">Fizzlot</h1>
    <p class="product-type">CBD GUMMIES</p>
    <p class="extract-pill">HIGN CLEARITY CBD EXTRACT</p>
    <div class="flavor-visual" role="img" aria-label="Basket of strawberries and blueberries with gummies and dripping pink syrup"></div>
    <p class="net-weight">NET WT.<br>2.5 OZ. (70G)</p>
    <p class="website">CORVANTACBD.COM</p>
    <div class="strength-badge"><span class="mg">250MG</span><span class="cbd">CBD</span></div>
  </section>

  <section class="bag bag--blue">
    <svg class="bag-art" viewBox="0 0 464 720" preserveAspectRatio="none" aria-hidden="true">
      <defs>
        <linearGradient id="lilacBody" x1="0" y1="0" x2="1" y2="1">
          <stop offset="0" stop-color="#d9d6f0"/>
          <stop offset="0.45" stop-color="#f4f3fb"/>
          <stop offset="1" stop-color="#a49ed8"/>
        </linearGradient>
      </defs>
      <rect width="464" height="720" fill="url(#lilacBody)"/>
      <rect x="0" y="0" width="464" height="110" fill="#d6d3ef" opacity="0.6"/>
      <rect x="16" y="66" width="432" height="4" fill="#ffffff" opacity="0.8"/>
      <polygon points="0,220 464,20 464,60 0,280" fill="#ffffff" opacity="0.55"/>
      <polygon points="0,300 464,70 464,90 0,330" fill="#a7a1da" opacity="0.5"/>
      <polygon points="0,720 0,690 464,520 464,560 120,720" fill="#ffffff" opacity="0.85"/>
      <polygon points="200,720 464,600 464,640 290,720" fill="#ffffff" opacity="0.7"/>
    </svg>
    <div class="brand"><span class="brand-dot"></span>Corvanta<br>CBD</div>
    <h1 class="flavor-title">Blue Raspberry</h1>
    <p class="product-type">CBD GUMMIES</p>
    <p class="extract-pill">HIGN CLEARITY CBD EXTRACT</p>
    <div class="flavor-visual" role="img" aria-label="Basket of blue raspberries with gummies and dripping purple syrup"></div>
    <p class="net-weight">NET WT.<br>2.5 OZ. (70G)</p>
    <p class="website">CORVANTACBD.COM</p>
    <div class="strength-badge"><span class="mg">250MG</span><span class="cbd">CBD</span></div>
  </section>

</main>
</body>
</html>
```